Bref créative
Business cards and stationary Hospitality group company in Mexico
subtitle is optional "Hospitalidad Hecho en Mexico"
I need double sided standard sized Business Card [3.5" x 2"]
I like the fonts used in my logo but we are open to new fonts or more than one if necessary
Modern
Gerardo Villena
4871 Almendros
Col. Santa Brígida
Monterrey, NL México
CP 67215
beto@qvral.mx
www.qvral.mx
I am looking for a modern design, I like those colors but feel free to play with the colors if you have an idea..
QV ALBERGANTE

```html
<!DOCTYPE html>
<html lang="es">
<head>
<meta charset="utf-8">
<title>QV Albergante — Papelería</title>
<link href="https://fonts.googleapis.com/css2?family=Montserrat:wght@400;500;600;700&display=swap" rel="stylesheet">
<style>
  :root{
    --bg:#eceef0;
    --paper:#ffffff;
    --ink:#2a2a2c;
    --orange:#f26522;
    --red:#e43a26;
    --grey:#8a8a8e;
    --faint:#e9e9ea;
  }
  *{margin:0;padding:0;box-sizing:border-box}
  html,body{width:1200px;height:936px;overflow:hidden;background:var(--bg);font-family:"Montserrat",sans-serif}
  .canvas{position:relative;width:1200px;height:936px}
  .piece{position:absolute;overflow:hidden;background:var(--paper)}
  .piece svg.art{position:absolute;inset:0;width:100%;height:100%}
  .brand{position:absolute;display:flex;align-items:center;gap:6px;font-weight:700;letter-spacing:.08em;white-space:nowrap}
  .brand .mark{width:10px;height:10px;background:var(--orange);flex:none}
  .brand-text{color:#fff}
  .small{position:absolute;font-size:6px;line-height:1.5;color:var(--grey);white-space:nowrap}

  .letterhead{left:177px;top:68px;width:395px;height:542px}
  .letterhead .brand{left:16px;top:30px;font-size:9px}
  .letterhead .watermark{position:absolute;left:0;right:0;top:245px;text-align:center;font-weight:700;font-size:30px;letter-spacing:.08em;color:var(--faint)}
  .letterhead .small{left:22px;top:455px}

  .folder{left:633px;top:38px;width:404px;height:595px;background:var(--ink)}
  .folder .brand{left:0;right:0;top:268px;justify-content:center;font-size:22px;gap:10px}
  .folder .brand .mark{width:18px;height:18px}

  .card{width:213px;height:104px;left:43px;background:var(--ink)}
  .card-front{top:658px}
  .card-back{top:782px}
  .card .small{color:#d8d8d8;font-size:5.5px;left:12px;top:22px}
  .card .name{position:absolute;right:12px;top:56px;font-size:7px;font-weight:600;color:var(--orange);white-space:nowrap}
  .card-front .brand{right:12px;top:24px;font-size:6.5px;gap:5px}
  .card-front .brand .mark{width:8px;height:8px}
  .card-back .brand{left:14px;top:22px;font-size:9px}

  .envelope{left:271px;top:668px;width:425px;height:205px}
  .envelope .brand{left:16px;top:12px;font-size:9px}
  .envelope .small{left:16px;top:182px}

  .envelope-back{left:734px;top:668px;width:427px;height:205px}
  .envelope-back .url{position:absolute;left:0;right:0;top:22px;text-align:center;color:#fff;font-size:10px;font-weight:500;letter-spacing:.28em}
</style>
</head>
<body>
<main class="canvas">

  <section class="piece letterhead">
    <svg class="art" viewBox="0 0 395 542" preserveAspectRatio="none" aria-hidden="true">
      <path d="M0 0H395V104C300 52 170 122 0 92Z" fill="var(--orange)"/>
      <path d="M0 0H395V92C300 44 170 112 0 84Z" fill="var(--paper)"/>
      <path d="M0 0H395V86C300 36 170 104 0 76Z" fill="var(--ink)"/>
      <path d="M0 542V512C140 530 270 480 395 424V542Z" fill="var(--orange)"/>
      <path d="M0 542V520C140 538 270 492 395 436V542Z" fill="var(--paper)"/>
      <path d="M0 542V526C140 542 270 500 395 446V542Z" fill="var(--ink)"/>
    </svg>
    <div class="brand"><span class="mark"></span><span class="brand-text">QV ALBERGANTE</span></div>
    <div class="watermark">QV ALBERGANTE</div>
    <p class="small">4871 Almendros, Col. Santa Brígida<br>Monterrey, NL México, CP 67215<br>+52 81 5550 2147<br>beto@qvral.mx<br>www.qvral.mx</p>
  </section>

  <section class="piece folder">
    <svg class="art" viewBox="0 0 404 595" preserveAspectRatio="none" aria-hidden="true">
      <path d="M0 0H210C110 20 40 70 0 190Z" fill="var(--orange)"/>
      <path d="M0 0H196C100 18 32 66 0 176Z" fill="var(--paper)"/>
      <path d="M0 595V556C150 560 300 520 404 420V595Z" fill="var(--paper)"/>
      <path d="M0 595V566C150 568 300 532 404 436V595Z" fill="var(--orange)"/>
      <path d="M0 595V584C170 586 310 556 404 488V595Z" fill="var(--red)"/>
    </svg>
    <div class="brand"><span class="mark"></span><span class="brand-text">QV ALBERGANTE</span></div>
  </section>

  <section class="piece card card-front">
    <svg class="art" viewBox="0 0 213 104" preserveAspectRatio="none" aria-hidden="true">
      <path d="M0 104V90C70 96 150 84 213 60V104Z" fill="var(--paper)"/>
      <path d="M0 104V94C70 100 150 90 213 68V104Z" fill="var(--orange)"/>
    </svg>
    <p class="small">4871 Almendros<br>Col. Santa Brígida<br>Monterrey, NL México<br>CP 67215<br>beto@qvral.mx</p>
    <div class="brand"><span class="mark"></span><span class="brand-text">QV ALBERGANTE</span></div>
    <p class="name">Gerardo Villena</p>
  </section>

  <section class="piece card card-back">
    <svg class="art" viewBox="0 0 213 104" preserveAspectRatio="none" aria-hidden="true">
      <path d="M0 104V92C70 98 150 86 213 62V104Z" fill="var(--paper)"/>
      <path d="M0 104V96C70 102 150 92 213 70V104Z" fill="var(--orange)"/>
    </svg>
    <div class="brand"><span class="mark"></span><span class="brand-text">QV ALBERGANTE</span></div>
  </section>

  <section class="piece envelope">
    <svg class="art" viewBox="0 0 425 205" preserveAspectRatio="none" aria-hidden="true">
      <path d="M0 0H425V22C320 30 200 30 0 60Z" fill="var(--orange)"/>
      <path d="M0 0H425V18C320 24 200 24 0 52Z" fill="var(--paper)"/>
      <path d="M0 0H425V14C320 20 200 18 0 46Z" fill="var(--ink)"/>
      <path d="M425 205V150C380 178 330 196 260 205Z" fill="var(--orange)"/>
      <path d="M425 205V166C390 186 350 200 300 205Z" fill="var(--ink)"/>
    </svg>
    <div class="brand"><span class="mark"></span><span class="brand-text">QV ALBERGANTE</span></div>
    <p class="small">4871 Almendros, Col. Santa Brígida, Monterrey, NL México, CP 67215</p>
  </section>

  <section class="piece envelope-back">
    <svg class="art" viewBox="0 0 427 205" preserveAspectRatio="none" aria-hidden="true">
      <path d="M0 0H427V54C300 78 130 78 0 54Z" fill="var(--orange)"/>
      <path d="M0 0H427V40C300 62 130 62 0 40Z" fill="var(--red)" opacity=".35"/>
    </svg>
    <p class="url">www.qvral.mx</p>
  </section>

</main>
</body>
</html>
```